IT Business Card Design

My company is a newly started small IT repair business. I operate outside of usual hours except for Saturday.
I am a very experienced and professional Technician.
I would like the business card to express that I am running a professional business and not some home IT business. This should be expressed through the design of the business card.
On the back of the card I would like the name of the company to be displayed.
Updates
Sorry guys, I have updated the requirement to be double sided. Fantastic submissions so far! Keep up the good work.
Hey designers!
Hey Designers!
Thank you all for your hard work!
Target Market(s)
Home to small business users.
Industry/Entity Type
Business
Contact Information for Business Card
Harbourline Computers
Marcus Pembrey (Director)
marcus.pembrey@quenmail.com.au
Operating Hours
5pm-12am Mon - Fri
9am - 5pm Sat
Mobile
0437915263
Requirements
Must have
- The base colour must be matte black. There must be some dark purple. (To go with the "Harbourline" theme)

```html
<!DOCTYPE html>
<html lang="en">
<head>
<meta charset="utf-8">
<title>Harbourline Computers — Business Card</title>
<link rel="stylesheet" href="https://fonts.googleapis.com/css2?family=Quicksand:wght@400;500;600&display=swap">
<style>
  :root {
    --backdrop: #d9d6d2;
    --card-black: #2b2a2a;
    --card-edge: #1f1e1e;
    --purple: #5a2a8c;
    --purple-soft: #3d2a5a;
    --text-light: #d8d6dc;
    --text-muted: #a9a6ad;
  }
  * { box-sizing: border-box; margin: 0; padding: 0; }
  html, body {
    width: 1200px;
    height: 873px;
    overflow: hidden;
  }
  body {
    background: var(--backdrop);
    font-family: "Quicksand", sans-serif;
    position: relative;
  }
  .card {
    position: absolute;
    width: 500px;
    height: 286px;
    background: var(--card-black);
    border-radius: 4px;
    box-shadow: 0 10px 28px rgba(0,0,0,0.28);
    color: var(--text-light);
  }
  .card--front { left: 70px; top: 294px; }
  .card--back  { left: 630px; top: 294px; }

  /* front */
  .brand {
    position: absolute;
    left: 34px;
    top: 30px;
    display: flex;
    align-items: center;
    gap: 12px;
  }
  .brand__mark {
    width: 34px;
    height: 34px;
    border-radius: 50%;
    border: 3px solid var(--purple);
  }
  .brand__name {
    font-size: 19px;
    font-weight: 500;
    color: var(--purple);
    letter-spacing: 0.3px;
  }
  .person {
    position: absolute;
    left: 34px;
    top: 92px;
  }
  .person__name {
    font-size: 18px;
    font-weight: 500;
    color: var(--purple);
  }
  .person__role {
    font-size: 11px;
    color: var(--text-muted);
    margin-top: 2px;
  }
  .contact {
    position: absolute;
    left: 34px;
    top: 150px;
  }
  .section-title {
    font-size: 16px;
    font-weight: 500;
    color: var(--purple);
    margin-bottom: 4px;
  }
  .contact__line, .hours__line {
    font-size: 12.5px;
    color: var(--text-light);
    line-height: 1.45;
  }
  .hours {
    position: absolute;
    left: 292px;
    top: 176px;
  }
  .desk-art {
    position: absolute;
    right: 30px;
    top: 56px;
    width: 180px;
    height: 110px;
    border-radius: 4px;
    background: linear-gradient(135deg, var(--purple-soft), rgba(61,42,90,0.45));
    opacity: 0.75;
  }

  /* back */
  .back-brand {
    position: absolute;
    left: 0;
    right: 0;
    top: 96px;
    display: flex;
    flex-direction: column;
    align-items: center;
  }
  .back-brand__row {
    display: flex;
    align-items: center;
    gap: 16px;
  }
  .back-brand__mark {
    width: 56px;
    height: 56px;
    border-radius: 50%;
    border: 4px solid var(--purple);
  }
  .back-brand__name {
    font-size: 30px;
    font-weight: 500;
    color: var(--purple);
    letter-spacing: 0.4px;
  }
  .back-brand__tagline {
    margin-top: 8px;
    margin-left: 72px;
    font-size: 13px;
    color: var(--text-muted);
    letter-spacing: 1.2px;
  }
</style>
</head>
<body>
  <section class="card card--front">
    <div class="brand">
      <span class="brand__mark"></span>
      <span class="brand__name">Harbourline Computers</span>
    </div>

    <div class="person">
      <p class="person__name">Marcus Pembrey</p>
      <p class="person__role">director</p>
    </div>

    <div class="contact">
      <p class="section-title">Contact</p>
      <p class="contact__line">marcus.pembrey@quenmail.com.au</p>
      <p class="contact__line">0437915263</p>
    </div>

    <div class="desk-art" role="img" aria-label="Faint purple illustration of a desktop computer with monitor and mouse"></div>

    <div class="hours">
      <p class="section-title">Operating Hours</p>
      <p class="hours__line">Monday - Friday</p>
      <p class="hours__line">5pm-12am</p>
      <p class="hours__line">Saturday</p>
      <p class="hours__line">9am - 5pm</p>
    </div>
  </section>

  <section class="card card--back">
    <div class="back-brand">
      <div class="back-brand__row">
        <span class="back-brand__mark"></span>
        <span class="back-brand__name">Harbourline Computers</span>
      </div>
      <p class="back-brand__tagline">experience &amp; professional</p>
    </div>
  </section>
</body>
</html>
```